Temporary fencing company needs a flyer design

We require a double sided DL flyer for our fencing company describing what we do, the areas we cover and a bit more information about the products we supply.

Target Market(s)

Residential customers, builders, commercial clients

Industry/Entity Type

Fencing

Requirements
Must have
• On the front we'd like the following:
• - the logo
• - the words "Temporary Fencing" which should stand out
• - the area we cover "Auckland Wide"
• - the words "Free Quotes" below that what we need for a quote, something like this:
• "
• Free Quotes
• All we need is the boundary length and the suburb! Tell us if the property is steep or something out of the ordinary.
• "
• Feel free to play around with the layout/wording, just needs to say that as the gist of the blurb.
• On the back:
• - The 0800 number: 0800 315 209
• - Info about our fencing:
• Standard panel set:
• 2.4 x 2.1m fence panel, concrete filled plastic foot and a clamp.
• Pedestrian gate:
• 2.4m wide fence panel with a hinged pedestrian gate that can be locked. Padlock supplied!
• Vehicle gate:
• 2.4m wide panel that is hinged for easy vehicle access. Padlock supplied!
• See our website for photos and the temporary fencing page for the various panels.
• On either side of the flyer we need some other contact details:
• Website - www.kestrelbarrierhire.co.nz
• Email - hire@kestrelbarrierhire.co.nz
• In terms of the colours:
• The logo and wording obviously has red and grey, use this as a guide, happy for other colours that work alongside these.
Nice to have
• Flyer should look professional.
Should not have
• Cartoony type of characters or fonts.

```html
<!DOCTYPE html>
<html lang="en">
<head>
<meta charset="utf-8">
<title>Kestrel Barrier – Temporary Fencing Flyer</title>
<link href="https://fonts.googleapis.com/css2?family=Roboto+Condensed:wght@400;700&family=Open+Sans:wght@400;700&display=swap" rel="stylesheet">
<style>
  :root {
    --red: #b3202a;
    --charcoal: #3b3b3b;
    --ink: #111111;
    --white: #ffffff;
    --photo-site: #8f9a86;
    --photo-site-light: #c9c9c4;
    --photo-studio: #e6e6e4;
    --photo-studio-accent: #e9693a;
    --photo-yard: #b7b8b4;
  }
  * { margin: 0; padding: 0; box-sizing: border-box; }
  html, body { width: 1200px; height: 2546px; overflow: hidden; background: var(--white); }
  .flyer {
    position: relative; width: 1200px; height: 2546px; background: var(--white);
    font-family: "Roboto Condensed", "Arial Narrow", sans-serif; color: var(--ink);
  }
  .photo { position: absolute; }
  .photo--site { left: 0; top: 0; width: 643px; height: 444px;
    background: linear-gradient(180deg, var(--photo-site) 0%, #6f7d5e 45%, var(--photo-site-light) 70%, #d4d4d0 100%); }
  .photo--studio { left: 684px; top: 0; width: 516px; height: 728px;
    background: linear-gradient(160deg, var(--photo-studio) 0%, #d9d9d7 75%, #ecc3ae 90%, var(--photo-studio-accent) 100%); }
  .photo--yard { left: 0; top: 1735px; width: 400px; height: 773px;
    background: linear-gradient(180deg, #a9b0b6 0%, var(--photo-yard) 55%, #d79a6c 80%, #c8b9a3 100%); }

  .call { position: absolute; left: 53px; top: 468px; }
  .call__label { font-size: 58px; line-height: 1; }
  .call__number { font-size: 100px; line-height: 1; margin-top: 22px; letter-spacing: 1px; }

  .product__tag {
    position: absolute; left: 0; height: 110px; background: var(--red); color: var(--white);
    border-radius: 0 56px 56px 0; font-size: 62px; line-height: 110px; padding-left: 62px;
  }
  .product__text { position: absolute; left: 53px; font-size: 56px; line-height: 72px; }
  .product__text--large { font-size: 61px; line-height: 73px; }

  .brand {
    position: absolute; left: 400px; top: 1735px; width: 800px; height: 334px;
    display: flex; align-items: center; justify-content: center; gap: 22px;
  }
  .brand__mark { width: 46px; height: 46px; background: var(--red); }
  .brand__name { font-size: 76px; font-weight: 700; color: var(--red); letter-spacing: 1px; }

  .contact {
    position: absolute; left: 400px; top: 2069px; width: 800px; height: 316px;
    background: var(--charcoal); color: var(--white); font-family: "Open Sans", Arial, sans-serif;
    padding: 44px 0 0 27px;
  }
  .contact__address { font-size: 48px; line-height: 58px; }
  .contact__label { font-size: 33px; font-weight: 700; margin-top: 30px; }
  .contact__email { font-size: 45px; margin-top: 10px; }

  .web {
    position: absolute; left: 400px; top: 2385px; width: 800px; height: 123px;
    font-family: "Open Sans", Arial, sans-serif; font-weight: 700; color: var(--red);
    font-size: 47px; line-height: 123px; padding-left: 16px;
  }
  .footer-band { position: absolute; left: 0; top: 2508px; width: 1200px; height: 38px; background: var(--red); }
</style>
</head>
<body>
<main class="flyer">
  <div class="photo photo--site" role="img" aria-label="Temporary fence panels on blue feet along a grassy bank at a building site"></div>
  <div class="photo photo--studio" role="img" aria-label="Close view of a mesh fence panel with brace stay and orange weighted feet"></div>

  <section class="call">
    <p class="call__label">Call Us</p>
    <p class="call__number">0800 315 209</p>
  </section>

  <h2 class="product__tag" style="top:730px;width:665px;">Standard panel set:</h2>
  <p class="product__text" style="top:848px;">2.4 x 2.1m fence panel, concrete filled<br>plastic foot and a clamp</p>

  <h2 class="product__tag" style="top:1022px;width:573px;">Pedestrian gate:</h2>
  <p class="product__text product__text--large" style="top:1148px;">2.4m wide fence panel with a hinged<br>pedestrian gate that can be locked.<br>Padlock supplied!</p>

  <h2 class="product__tag" style="top:1414px;width:488px;">Vehicle gate:</h2>
  <p class="product__text product__text--large" style="top:1566px;">2.4m wide panel that is hinged for easy<br>vehicle access. Padlock supplied!</p>

  <div class="photo photo--yard" role="img" aria-label="Hinged vehicle gate panels stacked beside orange feet in a yard"></div>

  <div class="brand">
    <span class="brand__mark"></span>
    <span class="brand__name">Kestrel Barrier</span>
  </div>

  <section class="contact">
    <p class="contact__address">PO Box 507316<br>Eastmere, Auckland.</p>
    <p class="contact__label">email:</p>
    <p class="contact__email">hire@kestrelbarrierhire.co.nz</p>
  </section>

  <p class="web">www.kestrelbarrierhire.co.nz</p>
  <div class="footer-band"></div>
</main>
</body>
</html>
```